Business Card and Letterhead for Zelvora - modern real estate business

I need a double sided business card design for Zelvora. Please see business card brief here https://files.quillnote-hub.net/page/7RtxQmZbn4LsWe2VyHoPk9dFjuC3gaXrTmqEi5Ns_pz/view?mode=shared

Please feel free to design the business cards however you feel best. I am happy to give some creative freedoms and then provide feedback from there.

Please then also create a letterhead to match the business card design

Colors

Designer to choose colors to be used in the design.

Requirements
Must have
• Must be a modern, elegant business card which looks very professional

```html
<!DOCTYPE html>
<html lang="en">
<head>
<meta charset="utf-8">
<title>Zelvora Business Card</title>
<link rel="stylesheet" href="https://fonts.googleapis.com/css2?family=Montserrat:wght@400;600;700&display=swap">
<style>
  :root {
    --page: #e9e9e9;
    --card-white: #ffffff;
    --brand-red: #e31e25;
    --card-black: #221f20;
    --ink-grey: #555555;
    --photo-light: #b8c7a4;
    --photo-dark: #3a3f45;
  }
  * { margin: 0; padding: 0; box-sizing: border-box; }
  html, body { width: 1200px; height: 801px; overflow: hidden; }
  body {
    background: var(--page);
    font-family: "Montserrat", sans-serif;
    position: relative;
  }
  .card {
    position: absolute;
    top: 245px;
    width: 540px;
    height: 310px;
    overflow: hidden;
    box-shadow: 0 6px 18px rgba(0,0,0,0.18);
  }
  .card--front { left: 40px; background: var(--card-white); }
  .card--back { left: 620px; background: var(--card-black); }

  .name-band {
    position: absolute;
    left: 0; top: 40px;
    width: 100%; height: 72px;
    background: var(--brand-red);
  }
  .agent-name {
    position: absolute;
    right: 30px; top: 49px;
    color: var(--card-white);
    font-weight: 700;
    font-size: 25px;
    letter-spacing: 0.3px;
  }
  .agent-title {
    position: absolute;
    right: 30px; top: 83px;
    color: var(--card-white);
    font-weight: 400;
    font-size: 13px;
  }
  .agent-photo {
    position: absolute;
    left: 66px; top: 54px;
    width: 116px; height: 116px;
    border-radius: 50%;
    border: 4px solid var(--card-white);
    outline: 1.5px solid var(--brand-red);
    background: linear-gradient(160deg, var(--photo-light) 0%, #8fa08a 45%, var(--photo-dark) 100%);
  }
  .front-wordmark {
    position: absolute;
    right: 30px; top: 152px;
    color: var(--brand-red);
    font-weight: 600;
    font-size: 44px;
    letter-spacing: 2px;
  }
  .contact-list {
    position: absolute;
    left: 168px; top: 212px;
    list-style: none;
    color: var(--ink-grey);
    font-size: 12px;
    line-height: 19px;
  }
  .contact-list li { display: flex; align-items: center; gap: 7px; }
  .contact-list svg { width: 11px; height: 11px; fill: var(--brand-red); flex: none; }
  .postal-address {
    position: absolute;
    left: 186px; top: 272px;
    color: var(--ink-grey);
    font-size: 12px;
  }
  .back-wordmark {
    position: absolute;
    left: 0; right: 0; top: 50%;
    transform: translateY(-50%);
    text-align: center;
    color: var(--brand-red);
    font-weight: 600;
    font-size: 76px;
    letter-spacing: 3px;
  }
</style>
</head>
<body>
  <section class="card card--front">
    <div class="name-band"></div>
    <p class="agent-name">Lachlan Reeve</p>
    <p class="agent-title">Licenced Real Estate Agent</p>
    <div class="agent-photo" role="img" aria-label="Portrait photo of the agent outdoors"></div>
    <p class="front-wordmark">ZELVORA</p>
    <ul class="contact-list">
      <li>
        <svg viewBox="0 0 24 24" aria-hidden="true"><path d="M6.6 10.8a15.1 15.1 0 0 0 6.6 6.6l2.2-2.2a1 1 0 0 1 1-.25 11.4 11.4 0 0 0 3.6.57 1 1 0 0 1 1 1V20a1 1 0 0 1-1 1A17 17 0 0 1 3 4a1 1 0 0 1 1-1h3.5a1 1 0 0 1 1 1c0 1.25.2 2.45.57 3.57a1 1 0 0 1-.25 1z"/></svg>
        <span>0400 318 592</span>
      </li>
      <li>
        <svg viewBox="0 0 24 24" aria-hidden="true"><path d="M2 5h20v14H2zm2 2v.5l8 5 8-5V7zm0 2.9V17h16V9.9l-8 5z"/></svg>
        <span>lachlan@zelvora.com</span>
      </li>
      <li>
        <svg viewBox="0 0 24 24" aria-hidden="true"><path d="M12 2a10 10 0 1 0 0 20 10 10 0 0 0 0-20zm6.9 6h-3a15 15 0 0 0-1.3-3.9A8 8 0 0 1 18.9 8zM12 4c.9 1.2 1.6 2.6 2 4h-4c.4-1.4 1.1-2.8 2-4zM4.3 14a8 8 0 0 1 0-4h3.4a16 16 0 0 0 0 4zm.8 2h3a15 15 0 0 0 1.3 3.9A8 8 0 0 1 5.1 16zm3-8h-3a8 8 0 0 1 4.3-3.9A15 15 0 0 0 8.1 8zM12 20c-.9-1.2-1.6-2.6-2-4h4c-.4 1.4-1.1 2.8-2 4zm2.3-6H9.7a14 14 0 0 1 0-4h4.6a14 14 0 0 1 0 4zm.3 5.9a15 15 0 0 0 1.3-3.9h3a8 8 0 0 1-4.3 3.9zm1.7-5.9a16 16 0 0 0 0-4h3.4a8 8 0 0 1 0 4z"/></svg>
        <span>www.zelvora.com</span>
      </li>
    </ul>
    <p class="postal-address">PO Box 1180 Larkfield NSW 2790</p>
  </section>

  <section class="card card--back">
    <p class="back-wordmark">ZELVORA</p>
  </section>
</body>
</html>
```